Ledgers On Track Business Card Design

We are a bookkeeping and accounting practice and are particularly passionate about Talvo as 'state of the art' accounting software. We offer a number of services which are listed on the back of the card. The logos for LOT have already been developed. There are also other logos of organisations we are involved with - Talvo (both certified advisor and silver partner), GFR, and filerite hub. Regarding colours, we would like to use the colours similar to our website, www.ledgersontrack.com, and these connect with the www.talvo.com.au website. The proposed layout as it is just does not look too great - it looks like an amateur has done it - which is true!

Industry/Entity Type

Accounting

Contact Information for Business Card

The details to appear on the card are found on the files uploaded. I have front and back rough layouts.

```html
<!DOCTYPE html>
<html lang="en">
<head>
<meta charset="utf-8">
<title>Ledgers On Track – Business Card</title>
<link rel="stylesheet" href="https://fonts.googleapis.com/css2?family=Bree+Serif&family=Questrial&display=swap">
<style>
  :root {
    --page-bg: #f2f4f6;
    --card-white: #ffffff;
    --brand-navy: #3f4f9a;
    --brand-green: #5fb330;
    --brand-cyan: #13b5ea;
    --brand-teal: #1a8fb0;
    --deep-teal: #0f6f8e;
    --badge-tint: #d9eef5;
    --text-slate: #3d4a78;
    --text-dark: #222a3a;
    --white: #ffffff;
  }
  * { box-sizing: border-box; margin: 0; padding: 0; }
  html, body { width: 1200px; height: 900px; overflow: hidden; }
  body {
    background: var(--page-bg);
    font-family: "Questrial", Arial, sans-serif;
    position: relative;
  }
  .card {
    position: absolute;
    top: 285px;
    width: 540px;
    height: 330px;
    border-radius: 22px;
    overflow: hidden;
    box-shadow: 0 10px 30px rgba(20, 40, 60, 0.15);
  }

  /* Front */
  .card-front { left: 45px; background: var(--card-white); }
  .front-band { position: absolute; left: 0; bottom: 0; width: 100%; height: 60px; }
  .brand-block { position: absolute; left: 30px; top: 52px; display: flex; align-items: center; gap: 18px; }
  .brand-square { width: 56px; height: 56px; background: var(--brand-green); border-radius: 4px; }
  .brand-name {
    font-family: "Bree Serif", Georgia, serif;
    font-size: 38px; line-height: 1.1; color: var(--brand-navy);
  }
  .holder { position: absolute; right: 28px; top: 24px; text-align: right; }
  .holder-name { color: var(--brand-cyan); font-size: 16px; margin-bottom: 3px; }
  .holder-meta { color: var(--text-slate); font-size: 12.5px; line-height: 1.45; }
  .contact-list { position: absolute; left: 26px; top: 160px; list-style: none; color: var(--text-slate); font-size: 14px; line-height: 1.32; }
  .contact-list li { display: flex; align-items: flex-start; gap: 6px; }
  .contact-list svg { width: 12px; height: 12px; margin-top: 3px; flex: none; fill: var(--brand-cyan); }
  .contact-list .indent { padding-left: 18px; }
  .contact-list .abn { font-size: 10px; padding-left: 18px; margin-top: 1px; }
  .partner-row { position: absolute; right: 28px; top: 178px; display: flex; align-items: center; gap: 10px; }
  .partner-name { font-size: 20px; color: var(--brand-cyan); }
  .plain-badge { width: 40px; height: 40px; border-radius: 6px; background: var(--badge-tint); }
  .filing-name { position: absolute; right: 30px; top: 232px; font-size: 19px; color: var(--text-dark); }
  .guild-name { position: absolute; right: 30px; top: 258px; font-size: 24px; color: var(--text-slate); }

  /* Back */
  .card-back {
    left: 615px;
    background: linear-gradient(180deg, var(--brand-cyan) 0%, var(--brand-teal) 55%, var(--deep-teal) 100%);
    color: var(--white);
    text-align: center;
  }
  .back-title { margin-top: 30px; font-family: "Bree Serif", Georgia, serif; font-weight: 400; font-size: 27px; }
  .service-list { list-style: none; margin-top: 18px; font-size: 15px; line-height: 1.55; }
  .back-partner { position: absolute; right: 26px; bottom: 40px; display: flex; align-items: center; gap: 10px; }
  .back-partner .partner-name { color: var(--white); }
  .back-partner .plain-badge { background: rgba(255, 255, 255, 0.35); }
</style>
</head>
<body>

<section class="card card-front" aria-label="Card front">
  <svg class="front-band" viewBox="0 0 540 60" preserveAspectRatio="none" aria-hidden="true">
    <path d="M0 22 Q270 48 540 30 L540 60 L0 60 Z" fill="#13b5ea"/>
    <path d="M0 40 Q270 58 540 46 L540 60 L0 60 Z" fill="#1a8fb0"/>
  </svg>

  <div class="brand-block">
    <div class="brand-square"></div>
    <div class="brand-name">Ledgers<br>On Track</div>
  </div>

  <div class="holder">
    <div class="holder-name">Martin Hale</div>
    <div class="holder-meta">B Comm MA PhD MGFR<br>Registered BAS agent</div>
  </div>

  <ul class="contact-list">
    <li><svg viewBox="0 0 12 12"><rect x="3" y="0.5" width="6" height="11" rx="1.2"/></svg>T 03 9517 2640</li>
    <li><svg viewBox="0 0 12 12"><path d="M2 1l2.5-.5 1.5 3-1.5 1a7 7 0 0 0 3 3l1-1.5 3 1.5-.5 2.5C5 11 1 7 2 1z"/></svg>M 0400 615 382</li>
    <li><svg viewBox="0 0 12 12"><path d="M0.5 2h11v8h-11z M0.5 2l5.5 4.5 5.5-4.5" stroke="#fff" stroke-width="0.8"/></svg>martin@ledgersontrack.com</li>
    <li><svg viewBox="0 0 12 12"><circle cx="6" cy="6" r="5.5"/><path d="M0.5 6h11M6 0.5v11" stroke="#fff" stroke-width="0.8"/></svg>www.ledgersontrack.com</li>
    <li><svg viewBox="0 0 12 12"><path d="M6 0.5L11.5 6H10v5.5H7.5V8h-3v3.5H2V6H0.5z"/></svg>18 Hillcrest Road,</li>
    <li class="indent">Elmvale VIC 3188</li>
    <li class="abn">ABN 62 508 117 934</li>
  </ul>

  <div class="partner-row">
    <span class="partner-name">Talvo</span>
    <div class="plain-badge"></div>
  </div>
  <div class="filing-name">filerite hub</div>
  <div class="guild-name">GFR</div>
</section>

<section class="card card-back" aria-label="Card back">
  <h1 class="back-title">Ledgers On Track</h1>
  <ul class="service-list">
    <li>Bookkeeping – data entry, bank reconciliation and review</li>
    <li>Payroll – Talvo Payroll Specialist</li>
    <li>BAS – GFR Public BAS Practitioner</li>
    <li>Training &amp; support – Talvo Certified Advisor</li>
    <li>Management reports</li>
    <li>Tax – filerite hub Member</li>
    <li>HR services</li>
  </ul>
  <div class="back-partner">
    <span class="partner-name">Talvo</span>
    <div class="plain-badge"></div>
  </div>
</section>

</body>
</html>
```